Book Cover Design Project

I need a book cover for a book that we will be releasing in the next few months.

It is a business book aimed at small businesses and people who want to escape the 9 - 5 and start their own business.

We want it to look similar to: http://www.tolvanbrook.example/wp-content/uploads/2010/03/fold-up.jpg and also the book designs that I have uploaded images for.

I quite like the grey / charcoal background and the bright lime green colours from the Quiet Harbor logo that I have attached. However, anything bright would be good - I am prepared to be flexible with colours. The books I have attached are a high impact as well - being bright blue with white black font with a really cool font.

The book is titled:

The Lantern Shop Plan

By Dale Vortan

Still thinking of the tagline, for now just use "Start an Online Business in no time at all"

Room for a quote/testimonial on the front of the book at the bottom, and as well on the back.

For the back cover text just use dummy text and my photo that is attached for now as well.

Barcode ISBN on the back at the bottom - price will be $19.95

Needs to be in PSD so we can change the text from our end.

I really want to get a good template made that I can edit the text for as we are still developing the book, but I want to get the book cover done so I can start advertising that it will be arriving soon.

There will probably be alterations that I need help with later down the track so looking to work with someone closely on this, and I will pay you for any extra time down the track..

Sizes will probably be around: I think 20.5cm tall and 14cm wide would be good..

Not sure how thick for the spine, it will depend on how many words get cut off, but as an estimate probably 1.5CM..
Updates

Just added some more detail to the brief.. Please read it carefully.

Target Market(s)

small business owners, professionals who want to start their own business, soon to be entrepreneurs, entrepreneurs

Industry/Entity Type

Advertising

Requirements
Must have
• The Lantern Shop Plan

and Dale Vortan must be prominent.

Tag line should be look cool under the title.

Must be very modern and cool. Needs to catch people's eyes so needs to be really punchy.

Nice to have
• Maybe a clock or stopwatch icon would be cool to add in there so it isn't just plain.. Similar to like how the books have a cool icon with them that I have attached in the uploaded images.
Should not have
• I like simplicity, artistic and very high impact. It really needs to draw you in and catch your eye.

Don't use plain boring fonts. Although I like simplicity slick design is very important - I dont want it to be boring - it has to look high quality and expensive. Therefore do not use fonts like Arial, Times New Roman those really boring fonts that make it look cheap. If I was going to do something like that then I might as well do it myself.

If you want to see the quality of things that I am usually involved with look at the artwork for one of my events that I run called Daybreaker: http://www.daybreaker.example/daybreaker-festival-anthems-ft-loomsparrow-harvest-night-eve-metro-report/

That will give you an idea of what type of quality things that I am involved with, so you need to be up for the task..

```html
<!DOCTYPE html>
<html lang="en">
<head>
<meta charset="utf-8">
<title>The Lantern Shop Plan — Book Cover</title>
<link rel="stylesheet" href="https://fonts.googleapis.com/css2?family=Antonio:wght@400;500&family=Roboto+Slab:wght@300;400;800&family=Arimo&display=swap">
<style>
  :root {
    --ink: #0c0c0c;
    --ink-soft: #151515;
    --paper: #ffffff;
    --lime: #c6f01a;
    --rule: #2a2a2a;
    --portrait-top: #8a8f94;
    --portrait-bottom: #3c3a38;
  }
  * { margin: 0; padding: 0; box-sizing: border-box; }
  html, body { width: 1200px; height: 834px; overflow: hidden; background: var(--ink); }
  .cover {
    position: relative;
    width: 1200px;
    height: 834px;
    background-color: var(--ink);
    background-image:
      linear-gradient(var(--ink-soft) 1px, transparent 1px),
      linear-gradient(90deg, var(--ink-soft) 1px, transparent 1px);
    background-size: 6px 6px;
    color: var(--paper);
    overflow: hidden;
  }
  .spine-edge {
    position: absolute;
    top: 0;
    width: 1px;
    height: 834px;
    background: var(--rule);
  }
  .spine-edge--left { left: 571px; }
  .spine-edge--right { left: 632px; }

  /* Back cover */
  .author-photo {
    position: absolute;
    left: 239px;
    top: 157px;
    width: 97px;
    height: 97px;
    border: 2px solid var(--lime);
    background: linear-gradient(180deg, var(--portrait-top), var(--portrait-bottom));
  }
  .blurb {
    position: absolute;
    left: 55px;
    top: 283px;
    width: 466px;
    font-family: "Roboto Slab", serif;
    font-weight: 300;
    font-size: 10.5px;
    line-height: 17px;
    letter-spacing: 1.6px;
    text-align: justify;
    hyphens: auto;
  }
  .testimonial {
    position: absolute;
    font-family: "Roboto Slab", serif;
    font-weight: 300;
    font-style: italic;
    font-size: 13.5px;
    letter-spacing: 1.8px;
    white-space: nowrap;
  }
  .testimonial--back { left: 48px; top: 407px; }
  .testimonial--front { left: 910px; top: 601px; transform: translateX(-50%); }
  .price {
    position: absolute;
    left: 398px;
    top: 632px;
    font-family: "Arimo", sans-serif;
    font-size: 27px;
    color: var(--lime);
  }
  .isbn-panel {
    position: absolute;
    left: 378px;
    top: 681px;
    width: 144px;
    height: 42px;
    background: var(--paper);
  }

  /* Front cover */
  .title {
    position: absolute;
    left: 918px;
    top: 62px;
    transform: translateX(-50%);
    font-family: "Antonio", sans-serif;
    font-weight: 400;
    text-align: center;
    line-height: 1;
    white-space: nowrap;
  }
  .title__line {
    display: block;
    font-size: 112px;
    height: 116px;
    letter-spacing: 3px;
  }
  .title__line--accent { color: var(--lime); letter-spacing: 6px; }
  .tagline {
    position: absolute;
    left: 917px;
    top: 525px;
    transform: translateX(-50%);
    font-family: "Roboto Slab", serif;
    font-weight: 800;
    font-size: 12.5px;
    letter-spacing: 1.2px;
    text-transform: uppercase;
    white-space: nowrap;
  }
  .divider {
    position: absolute;
    left: 733px;
    top: 697px;
    width: 372px;
    height: 1px;
    background: var(--rule);
  }
  .clock-icon {
    position: absolute;
    left: 893px;
    top: 672px;
    width: 44px;
    height: 46px;
  }
  .byline {
    position: absolute;
    left: 920px;
    top: 718px;
    transform: translateX(-50%);
    font-family: "Antonio", sans-serif;
    font-weight: 400;
    font-size: 86px;
    line-height: 1;
    letter-spacing: 3px;
    color: var(--lime);
    white-space: nowrap;
  }
</style>
</head>
<body>
<main class="cover">
  <div class="spine-edge spine-edge--left"></div>
  <div class="spine-edge spine-edge--right"></div>

  <section class="back-cover">
    <div class="author-photo" role="img" aria-label="Author portrait photograph"></div>
    <p class="blurb">Lorem Ipsum is simply dummy text of the printing and typesetting industry. Lorem Ipsum has been the industry's standard dummy text ever since the 1500s, when an unknown printer took a galley of type and scrambled it to make a type specimen book. It has survived not only five centuries, but also the leap into electronic typesetting, remaining essentially unchanged.</p>
    <p class="testimonial testimonial--back">“Room for quote/testimonial”</p>
    <p class="price">$19.95</p>
    <div class="isbn-panel"></div>
  </section>

  <section class="front-cover">
    <h1 class="title">
      <span class="title__line">THE</span>
      <span class="title__line">LANTERN</span>
      <span class="title__line">SHOP</span>
      <span class="title__line title__line--accent">PLAN</span>
    </h1>
    <p class="tagline">Start an online business in no time at all</p>
    <p class="testimonial testimonial--front">“Room for quote/testimonial”</p>
    <div class="divider"></div>
    <svg class="clock-icon" viewBox="0 0 44 46" aria-hidden="true">
      <circle cx="10" cy="8" r="6" fill="#e8e8e8" stroke="#555" stroke-width="1.5"/>
      <circle cx="34" cy="8" r="6" fill="#e8e8e8" stroke="#555" stroke-width="1.5"/>
      <line x1="12" y1="40" x2="8" y2="45" stroke="#ccc" stroke-width="2.5" stroke-linecap="round"/>
      <line x1="32" y1="40" x2="36" y2="45" stroke="#ccc" stroke-width="2.5" stroke-linecap="round"/>
      <circle cx="22" cy="25" r="16" fill="#f4f4f4" stroke="#777" stroke-width="2"/>
      <line x1="22" y1="25" x2="22" y2="15" stroke="#333" stroke-width="1.8" stroke-linecap="round"/>
      <line x1="22" y1="25" x2="29" y2="27" stroke="#333" stroke-width="1.8" stroke-linecap="round"/>
      <circle cx="22" cy="25" r="1.5" fill="#333"/>
    </svg>
    <p class="byline">BY DALE VORTAN</p>
  </section>
</main>
</body>
</html>
```